Business Cards, Stationery, Email signature
and Stationary
Business Cards, Stationery, Email signature - Construction
Creative Brief
Use specific fonts
looking for strong bold lettering
Bright & Fun-filled
Marta Quillen
President
2873 E Marlow Street Orange, CA 94153
marta@larkwoodltdroofing.com
larkwoodltdroofing.com
Was considering having a black business cards so I really wanted to logo to "pop". Even though we are construction I love a card that has personality and fun.

```html
<!DOCTYPE html>
<html lang="en">
<head>
<meta charset="utf-8">
<title>Larkwood Ltd Stationery</title>
<link rel="stylesheet" href="https://fonts.googleapis.com/css2?family=Cinzel:wght@700&family=Open+Sans:wght@400;600&display=swap">
<style>
:root{
  --stage:#e9e2d6;
  --card-black:#0d0d0f;
  --blue:#1f8fd8;
  --blue-dark:#0b4f8c;
  --gold:#e8b640;
  --paper:#ffffff;
  --ink:#3a3f47;
  --muted:#8a929c;
  --label:#5b5347;
}
*{margin:0;padding:0;box-sizing:border-box}
html,body{width:1200px;height:439px;overflow:hidden;background:var(--stage);font-family:"Open Sans",sans-serif}
.canvas{position:relative;width:1200px;height:439px}
.brand{font-family:"Cinzel",serif;font-weight:700;color:var(--gold);letter-spacing:.5px;white-space:nowrap}
.mark{display:inline-block;border-radius:50%;background:var(--gold);vertical-align:middle}
.label{position:absolute;font-size:7px;color:var(--label);text-align:center;white-space:nowrap}

/* business cards */
.card{position:absolute;left:24px;width:170px;height:96px;background:var(--card-black);border-radius:4px;color:#cfd4da;overflow:hidden;box-shadow:0 2px 4px rgba(0,0,0,.35)}
.card .strip{position:absolute;left:0;top:0;bottom:0;width:12px;background:linear-gradient(var(--blue),var(--blue-dark))}
.card .head{position:absolute;left:20px;top:9px;font-size:10px}
.card .head .mark{width:11px;height:11px;margin-right:4px}
.card .info{position:absolute;left:20px;top:32px;font-size:5px;line-height:7.5px;white-space:nowrap}
.card .who{position:absolute;right:8px;top:38px;text-align:right;font-size:5px;line-height:7.5px;white-space:nowrap}
.card .who b{color:var(--blue);font-weight:600;font-size:6.5px}
.card-back{display:flex;flex-direction:column;align-items:center;justify-content:center;gap:5px}
.card-back .mark{width:30px;height:30px}
.card-back .brand{font-size:11px}
.card-back .web{font-size:5px;color:var(--muted)}

/* letterheads */
.letterhead{position:absolute;top:24px;width:262px;height:350px;background:var(--paper);box-shadow:0 2px 5px rgba(0,0,0,.25);overflow:hidden}
.letterhead .strip{position:absolute;left:0;top:0;bottom:0;width:18px;background:linear-gradient(var(--blue-dark),var(--blue) 60%,#7cc6f0)}
.letterhead .head{position:absolute;left:28px;top:14px;font-size:10px}
.letterhead .head .mark{width:12px;height:12px;margin-right:4px}
.letterhead .contact{position:absolute;left:160px;top:10px;font-size:4.5px;line-height:7px;color:var(--ink);white-space:nowrap}
.letterhead .faint{position:absolute;left:72px;top:110px;width:130px;height:130px;border-radius:50%;background:radial-gradient(rgba(232,182,64,.18),rgba(31,143,216,.08));display:flex;align-items:center;justify-content:center}
.letterhead .faint span{font-family:"Cinzel",serif;font-weight:700;font-size:12px;color:rgba(31,143,216,.15);white-space:nowrap}
.letterhead .foot{position:absolute;left:28px;bottom:10px;font-size:4.5px;color:var(--muted);white-space:nowrap}

/* envelopes */
.envelope{position:absolute;left:818px;width:370px;background:var(--paper);box-shadow:0 2px 5px rgba(0,0,0,.25);overflow:hidden}
.envelope svg{position:absolute;left:0;top:0}
.envelope .addr{position:absolute;font-size:7px}
.envelope .addr .mark{width:8px;height:8px;margin-right:3px}
.envelope .ret{position:absolute;font-size:4.5px;color:var(--muted);white-space:nowrap}
</style>
</head>
<body>
<div class="canvas">

  <div class="card" style="top:67px">
    <div class="strip"></div>
    <div class="head"><span class="mark"></span><span class="brand">Larkwood Ltd</span></div>
    <div class="info">2873 E Marlow Street<br>Orange, CA 94153<br>P: 555.210.4487<br>F: 555.210.4488</div>
    <div class="who"><b>Marta Quillen</b><br>President<br>marta@larkwoodltdroofing.com<br>larkwoodltdroofing.com</div>
  </div>
  <div class="label" style="left:24px;top:166px;width:170px">Business Card (front)</div>

  <div class="card" style="top:180px">
    <div class="strip"></div>
    <div class="head"><span class="mark"></span><span class="brand">Larkwood Ltd</span></div>
    <div class="info">2873 E Marlow Street<br>Orange, CA 94153<br>P: 555.210.4487<br>F: 555.210.4488</div>
    <div class="who"><b>Marta Quillen</b><br>President<br>marta@larkwoodltdroofing.com<br>larkwoodltdroofing.com</div>
  </div>
  <div class="label" style="left:24px;top:279px;width:170px">Business Card (option B)</div>

  <div class="card card-back" style="top:293px">
    <span class="mark"></span>
    <span class="brand">Larkwood Ltd</span>
    <span class="web">larkwoodltdroofing.com</span>
  </div>
  <div class="label" style="left:24px;top:392px;width:170px">Business Card (back)</div>

  <div class="letterhead" style="left:212px">
    <div class="strip"></div>
    <div class="head"><span class="mark"></span><span class="brand">Larkwood Ltd</span></div>
    <div class="contact">P: 555.210.4487<br>F: 555.210.4488<br>larkwoodltdroofing.com<br>Orange, CA 94153</div>
    <div class="faint" role="img" aria-label="Faint company emblem backdrop"><span>Larkwood Ltd</span></div>
    <div class="foot">2873 E Marlow Street, Orange, CA 94153</div>
  </div>
  <div class="label" style="left:212px;top:410px;width:262px">Letterhead (option A)</div>

  <div class="letterhead" style="left:497px">
    <div class="strip"></div>
    <div class="faint" role="img" aria-label="Faint company emblem backdrop"><span>Larkwood Ltd</span></div>
    <div class="foot">2873 E Marlow Street, Orange, CA 94153 · P: 555.210.4487</div>
  </div>
  <div class="label" style="left:497px;top:410px;width:262px">Letterhead (option B)</div>

  <div class="envelope" style="top:29px;height:90px">
    <svg width="370" height="90" viewBox="0 0 370 90"><defs><linearGradient id="fo" x1="0" y1="0" x2="0" y2="1"><stop offset="0" stop-color="#f6c36a"/><stop offset="1" stop-color="#e88a1e"/></linearGradient></defs><path d="M0 0H370V20L185 62 0 20Z" fill="url(#fo)"/></svg>
  </div>
  <div class="envelope" style="top:76px;height:96px">
    <svg width="370" height="96" viewBox="0 0 370 96"><defs><linearGradient id="fb" x1="0" y1="0" x2="0" y2="1"><stop offset="0" stop-color="#7cc6f0"/><stop offset="1" stop-color="#0b4f8c"/></linearGradient></defs><path d="M0 0H370V16L185 56 0 16Z" fill="url(#fb)"/></svg>
    <div class="addr" style="left:150px;top:70px"><span class="mark"></span><span class="brand">Larkwood Ltd</span></div>
  </div>
  <div class="envelope" style="top:180px;height:80px">
    <div class="addr" style="left:12px;top:10px"><span class="mark"></span><span class="brand">Larkwood Ltd</span></div>
    <div class="ret" style="left:12px;top:24px">2873 E Marlow Street, Orange, CA 94153</div>
  </div>
  <div class="envelope" style="top:228px;height:82px">
    <svg width="370" height="82" viewBox="0 0 370 82"><path d="M0 0L185 34 370 0" fill="none" stroke="#d5dbe2" stroke-width="1"/></svg>
    <div class="ret" style="left:12px;bottom:8px">larkwoodltdroofing.com · P: 555.210.4487</div>
  </div>
  <div class="label" style="left:818px;top:410px;width:370px">Envelope (front &amp; back)</div>

</div>
</body>
</html>
```